'Ormel Property Development' Business Card

Business Card Features:

High Quality (potentially textured) thick card - preference is white textured card

Logo (supplied)

We plan to use the vertical logo as the main logo. But i am happy for people to use either if they find it works better for the design of the card.

The building icon and also the insert to the 'E' is in a metallic finish, i think this should be finished in a metallic embossed or raised style.
Updates

Please note i have attached both a horizontal and Vertical Logo for your reference. We plan to use the vertical logo as the main logo. But i am happy for people to use either if they find it works better for the design of the card.

Please note i am considering having the cards made on stainless steel. This introduces the option of having cut outs in the card and etching or printing for the design. If you have a good concept for this please submit.

http://www.tinquarry.example/black-metal-cards# this is a site that makes the metal cards to offer some direction . . . . Please note i am basic the selection o the best design, if that means normal print cards on paper then this is what i will choose. But there are some great options with the metal. Thanks.

Industry/Entity Type

Building

Requirements
Must have
• Helvetica font to details side of card - logo as supplied to opposite side.

Card Details:

Darrow Pketts
Managing Director

+61 487 263 518
+61 3 6172 4809

PO Box 73
Bentleigh, VIC 3024

darrow@ormel.example

www.ormel.example

```html
<!DOCTYPE html>
<html lang="en">
<head>
<meta charset="utf-8">
<title>Ormel Property Development – Business Card</title>
<link rel="stylesheet" href="https://fonts.googleapis.com/css2?family=Arimo:wght@400;700&display=swap">
<style>
  :root {
    --canvas: #e9e8e6;
    --card: #fbfbfb;
    --ink: #2f2f2f;
    --ink-soft: #555555;
    --rule: #3a3a3a;
    --shadow: rgba(0, 0, 0, 0.18);
  }
  * { box-sizing: border-box; margin: 0; padding: 0; }
  html, body {
    width: 1200px;
    height: 800px;
    overflow: hidden;
    background: var(--canvas);
    font-family: "Arimo", Helvetica, Arial, sans-serif;
    color: var(--ink);
  }
  .canvas { position: relative; width: 1200px; height: 800px; }

  .card {
    position: absolute;
    width: 520px;
    height: 300px;
    background: var(--card);
    box-shadow: 0 6px 18px var(--shadow);
  }
  .card--front { left: 70px; top: 90px; }
  .card--back  { left: 610px; top: 410px; }

  .brand {
    display: flex;
    flex-direction: column;
    align-items: center;
    gap: 10px;
    color: var(--ink);
    font-weight: 700;
  }
  .brand__row { display: flex; align-items: center; gap: 12px; }
  .brand__mark { width: 22px; height: 22px; background: var(--ink); }
  .brand__name { font-size: 54px; letter-spacing: 4px; line-height: 1; }
  .brand__tagline { font-size: 15px; letter-spacing: 1px; }

  .card--front .brand {
    position: absolute;
    left: 0; right: 0; top: 50%;
    transform: translateY(-50%);
  }

  .card--back .brand {
    position: absolute;
    left: 0; width: 270px; top: 50%;
    transform: translateY(-50%);
  }
  .card--back .brand__name { font-size: 44px; letter-spacing: 3px; }
  .card--back .brand__tagline { font-size: 13px; }
  .card--back .brand__mark { width: 18px; height: 18px; }

  .divider {
    position: absolute;
    left: 280px; top: 34px; bottom: 34px;
    width: 1.5px;
    background: var(--rule);
  }

  .details {
    position: absolute;
    left: 300px; top: 44px; right: 20px;
  }
  .details__name { font-size: 24px; font-weight: 700; line-height: 1.1; }
  .details__title { font-size: 15px; color: var(--ink-soft); margin-top: 2px; }

  .contact { list-style: none; margin-top: 52px; }
  .contact__item {
    display: flex;
    align-items: center;
    gap: 6px;
    font-size: 11px;
    font-weight: 700;
    line-height: 17px;
  }
  .contact__icon { width: 11px; height: 11px; flex: none; }
</style>
</head>
<body>
<main class="canvas">

  <section class="card card--front" aria-label="Card front">
    <div class="brand">
      <div class="brand__row">
        <span class="brand__mark"></span>
        <span class="brand__name">ORMEL</span>
      </div>
      <span class="brand__tagline">Property Development</span>
    </div>
  </section>

  <section class="card card--back" aria-label="Card back">
    <div class="brand">
      <div class="brand__row">
        <span class="brand__mark"></span>
        <span class="brand__name">ORMEL</span>
      </div>
      <span class="brand__tagline">Property Development</span>
    </div>

    <div class="divider"></div>

    <div class="details">
      <h1 class="details__name">Darrow Pketts</h1>
      <p class="details__title">Managing Director</p>

      <ul class="contact">
        <li class="contact__item">
          <svg class="contact__icon" viewBox="0 0 12 12"><rect x="3" y="0.5" width="6" height="11" rx="1" fill="none" stroke="currentColor" stroke-width="1.2"/><line x1="5" y1="9.7" x2="7" y2="9.7" stroke="currentColor"/></svg>
          0487263518
        </li>
        <li class="contact__item">
          <svg class="contact__icon" viewBox="0 0 12 12"><path d="M2.5 1 L4.5 1 L5.2 3.8 L3.9 4.8 Q5 7.2 7.2 8.2 L8.2 6.9 L11 7.6 L11 9.6 Q10.6 11 9 11 Q1 10 1 2.8 Q1 1.2 2.5 1 Z" fill="currentColor"/></svg>
          1800 613 724
        </li>
        <li class="contact__item">
          <svg class="contact__icon" viewBox="0 0 12 12"><path d="M6 11.5 Q2 7 2 4.5 A4 4 0 0 1 10 4.5 Q10 7 6 11.5 Z" fill="currentColor"/><circle cx="6" cy="4.5" r="1.5" fill="var(--card)"/></svg>
          PO BOX 73 Bentleigh, VIC 3024
        </li>
        <li class="contact__item">
          <svg class="contact__icon" viewBox="0 0 12 12"><rect x="0.5" y="2" width="11" height="8" fill="currentColor"/><path d="M0.5 2 L6 6.5 L11.5 2" fill="none" stroke="var(--card)" stroke-width="1"/></svg>
          darrow@ormel.example
        </li>
        <li class="contact__item">
          <svg class="contact__icon" viewBox="0 0 12 12"><rect x="0.8" y="1" width="10.4" height="7.5" fill="none" stroke="currentColor" stroke-width="1.2"/><rect x="4" y="10" width="4" height="1.3" fill="currentColor"/></svg>
          www.ormel.example
        </li>
      </ul>
    </div>
  </section>

</main>
</body>
</html>
```